Electrical Panel Hazard

We are looking for a mail out flyer explaining common household electrical panels are now deemed a fire hazard making homes containing these panels unable to be insured. We are looking to have clients check their home for a panel or breaker made by
Granite Meridian, Pathwarden, Vorlex, Brackmoor or Gript-hold. The final design should inform clients of the hazard and recommend an inspection and possible replacement.

Company name: Oakhurst Building Services Inc
Phone Number: (555)-204-3187

Industry/Entity Type

Electrical

```html
<!DOCTYPE html>
<html lang="en">
<head>
<meta charset="utf-8">
<title>Oakhurst Building Services Inc – Electrical Panel Hazard</title>
<link rel="stylesheet" href="https://fonts.googleapis.com/css2?family=Bebas+Neue&family=Roboto:wght@400;500;700&family=Michroma&display=swap">
<style>
  :root {
    --navy: #0b2a6b;
    --navy-deep: #061d55;
    --royal: #0d4ea6;
    --orange: #f7941d;
    --ink-blue: #2e3192;
    --grey-text: #555555;
    --paper: #f2f2f2;
    --white: #ffffff;
  }
  * { margin: 0; padding: 0; box-sizing: border-box; }
  html, body { width: 1006px; height: 1200px; overflow: hidden; background: var(--paper); }
  .flyer { position: relative; width: 1006px; height: 1200px; background: var(--paper); overflow: hidden; }
  .hero { position: absolute; left: 0; top: 0; width: 1006px; height: 600px; }
  .brand {
    position: absolute; top: 42px; right: 34px;
    font-family: "Michroma", sans-serif; color: var(--white);
    font-size: 21px; line-height: 33px; text-align: right; letter-spacing: 0.5px;
  }
  .headline {
    position: absolute; top: 548px; left: 0; width: 100%; text-align: center;
    font-family: "Bebas Neue", sans-serif; font-weight: 400; font-size: 84px; line-height: 84px;
    color: var(--ink-blue); white-space: nowrap;
  }
  .notice {
    position: absolute; top: 637px; left: 0; width: 100%; text-align: center;
    font-family: "Roboto", sans-serif; font-weight: 500; font-size: 21px;
    line-height: 33px; color: var(--grey-text); white-space: nowrap;
  }
  .brands {
    position: absolute; top: 746px; left: 0; width: 100%;
    display: flex; justify-content: center; gap: 17px; list-style: none;
    font-family: "Roboto", sans-serif; font-weight: 500; font-size: 22px; line-height: 28px; color: var(--ink-blue);
  }
  .brands li { display: flex; align-items: center; gap: 8px; white-space: nowrap; }
  .brands svg { width: 19px; height: 19px; }
  .promise {
    position: absolute; top: 786px; left: 0; width: 100%; text-align: center;
    font-family: "Roboto", sans-serif; font-weight: 500; font-size: 20.5px; line-height: 26px;
    color: var(--orange); white-space: nowrap;
  }
  .thumb {
    position: absolute; top: 852px; width: 224px; height: 222px; border-radius: 50%;
    border: 7px solid var(--white); box-shadow: -5px 0 0 var(--orange);
  }
  .thumb-shadow {
    position: absolute; top: 1076px; width: 170px; height: 14px; border-radius: 50%;
    background: radial-gradient(ellipse at center, rgba(0,0,0,0.28), rgba(0,0,0,0) 70%);
  }
  .thumb-panel { left: 75px; background: radial-gradient(circle at 45% 45%, #6d6a66, #2c2a29 70%, #8a3a2a); }
  .thumb-meter { left: 393px; background: linear-gradient(135deg, #3a3f46, #d9b22e 45%, #2f6fc4 75%, #1e2430); }
  .thumb-burnt { left: 695px; background: radial-gradient(circle at 55% 50%, #4a3b34, #23201e 65%, #7d4a2c); }
  .footer {
    position: absolute; left: 0; top: 1101px; width: 1006px; height: 99px;
    background: linear-gradient(90deg, var(--royal), var(--navy-deep));
    display: flex; align-items: center; justify-content: space-between; padding: 4px 34px 0 27px;
    font-family: "Bebas Neue", sans-serif; font-weight: 400; font-size: 44px; line-height: 1; color: var(--orange);
    white-space: nowrap;
  }
  .footer .phone { display: flex; align-items: center; gap: 22px; }
  .footer svg { width: 40px; height: 40px; margin-top: -4px; }
</style>
</head>
<body>
<main class="flyer">
  <svg class="hero" viewBox="0 0 1006 600" xmlns="http://www.w3.org/2000/svg">
    <defs>
      <linearGradient id="headerFill" x1="0" y1="0" x2="1" y2="0">
        <stop offset="0" stop-color="#0d4ea6"/>
        <stop offset="1" stop-color="#061d55"/>
      </linearGradient>
      <linearGradient id="photoFill" x1="0" y1="0" x2="1" y2="0.3">
        <stop offset="0" stop-color="#d8b65a"/>
        <stop offset="0.35" stop-color="#4a4640"/>
        <stop offset="0.6" stop-color="#a98a6c"/>
        <stop offset="1" stop-color="#b3262f"/>
      </linearGradient>
    </defs>
    <path d="M0,0 H1006 V560 L1006,310 C700,145 300,100 0,112 Z" fill="url(#headerFill)"/>
    <path d="M0,112 C300,100 700,145 1006,310 V560 H0 Z" fill="var(--white)"/>
    <path d="M0,124 C300,112 700,160 1006,324 V519 Q503,407 0,546 Z" fill="url(#photoFill)"
          role="img" aria-label="Photo: two electricians in hard hats inspecting an open home breaker panel"/>
    <path d="M0,116 C300,104 700,150 1006,314" fill="none" stroke="var(--orange)" stroke-width="13"/>
    <path d="M0,546 Q503,407 1006,519 V530 Q503,430 0,552 Z" fill="var(--royal)"/>
    <path d="M0,552 Q503,430 1006,530 V573 Q503,455 0,584 Z" fill="var(--orange)"/>
    <path d="M0,584 Q503,455 1006,573 V600 H0 Z" fill="var(--paper)"/>
  </svg>

  <div class="brand">Oakhurst Building<br>Services Inc</div>

  <h1 class="headline">IS YOUR HOUSE SAFE?</h1>

  <p class="notice">
    NEW INSURANCE CODE MAY HAVE DEEMED YOUR HOMES ELECTRICAL PANEL<br>
    A FIRE HAZARD AND UNINSURABLE.<br>
    CALL US IF YOUR HOMES ELECTRICAL PANEL OR BREAKERS ARE MADE BY:
  </p>

  <ul class="brands">
    <li><svg viewBox="0 0 20 20"><rect x="2" y="3" width="14" height="14" rx="3" fill="none" stroke="currentColor" stroke-width="2"/><path d="M5 10 l3 3 l9-9" fill="none" stroke="currentColor" stroke-width="2.2"/></svg>GRANITE MERIDIAN</li>
    <li><svg viewBox="0 0 20 20"><rect x="2" y="3" width="14" height="14" rx="3" fill="none" stroke="currentColor" stroke-width="2"/><path d="M5 10 l3 3 l9-9" fill="none" stroke="currentColor" stroke-width="2.2"/></svg>PATHWARDEN</li>
    <li><svg viewBox="0 0 20 20"><rect x="2" y="3" width="14" height="14" rx="3" fill="none" stroke="currentColor" stroke-width="2"/><path d="M5 10 l3 3 l9-9" fill="none" stroke="currentColor" stroke-width="2.2"/></svg>VORLEX</li>
    <li><svg viewBox="0 0 20 20"><rect x="2" y="3" width="14" height="14" rx="3" fill="none" stroke="currentColor" stroke-width="2"/><path d="M5 10 l3 3 l9-9" fill="none" stroke="currentColor" stroke-width="2.2"/></svg>BRACKMOOR</li>
    <li><svg viewBox="0 0 20 20"><rect x="2" y="3" width="14" height="14" rx="3" fill="none" stroke="currentColor" stroke-width="2"/><path d="M5 10 l3 3 l9-9" fill="none" stroke="currentColor" stroke-width="2.2"/></svg>GRIPT-HOLD</li>
  </ul>

  <p class="promise">
    We are a fully state licensed electrical contracting company that<br>
    guarantees the best service with the lowest prices!
  </p>

  <div class="thumb thumb-panel" role="img" aria-label="Photo: close-up of an old breaker panel"></div>
  <div class="thumb-shadow" style="left:102px"></div>
  <div class="thumb thumb-meter" role="img" aria-label="Photo: hands testing a panel with a yellow multimeter"></div>
  <div class="thumb-shadow" style="left:420px"></div>
  <div class="thumb thumb-burnt" role="img" aria-label="Photo: heat-damaged breakers inside a panel"></div>
  <div class="thumb-shadow" style="left:722px"></div>

  <footer class="footer">
    <span class="cta">CALL US TODAY FOR YOUR FREE ESTIMATE!</span>
    <span class="phone">
      <svg viewBox="0 0 40 40"><circle cx="20" cy="20" r="17" fill="none" stroke="currentColor" stroke-width="3"/><path d="M14 11 l4 0 l2 5 l-3 2 q2 4 6 6 l2-3 l5 2 l0 4 q-1 2 -4 2 q-14 -2 -15 -15 q0-3 3-3 z" fill="currentColor"/></svg>
      <span class="number">(555)-204-3187</span>
    </span>
  </footer>
</main>
</body>
</html>
```